VOIP company busioness card redesign

Redesign business card to match our new logo and marketing material. Should include logo on one side and contact information on other side.

We like modern and clean

Industry/Entity Type

Phone Company

Contact Information for Business Card

One side should be logo other side should include contact info
Name
Phone Number
email
website

Font styles to use
Other font styles liked:
• dont care

Requirements
Must have
• Modern sleek design that works with our logo

```html
<!DOCTYPE html>
<html lang="en">
<head>
<meta charset="utf-8">
<title>Nimbra Business Card</title>
<link href="https://fonts.googleapis.com/css2?family=Lato:wght@300;400;700;900&display=swap" rel="stylesheet">
<style>
  :root {
    --page: #ecebe8;
    --paper: #f7f7f6;
    --blue: #11b3e0;
    --blue-deep: #0a8fc4;
    --blue-light: #19c5ea;
    --green: #9dc43c;
    --grey: #9a9a9a;
    --white: #ffffff;
  }
  * { box-sizing: border-box; margin: 0; padding: 0; }
  html, body { width: 1200px; height: 780px; overflow: hidden; }
  body {
    background: var(--page);
    font-family: "Lato", sans-serif;
    display: flex;
    align-items: center;
    justify-content: center;
    gap: 40px;
  }
  .card {
    position: relative;
    width: 540px;
    height: 310px;
    background: var(--paper);
    box-shadow: 0 10px 26px rgba(0,0,0,.18);
    overflow: hidden;
  }

  /* Front: contact side */
  .front .name-block {
    position: absolute; top: 26px; right: 30px; text-align: right;
  }
  .front .person { color: var(--blue); font-weight: 700; font-size: 20px; letter-spacing: .5px; }
  .front .role { color: var(--green); font-size: 13px; font-weight: 400; }
  .wordmark {
    color: var(--blue);
    font-weight: 900;
    letter-spacing: -1px;
    line-height: 1;
    display: flex; align-items: center; gap: 10px;
  }
  .wordmark .dot {
    width: 14px; height: 14px; border-radius: 50%; background: var(--green);
  }
  .front .wordmark { position: absolute; left: 30px; top: 52px; font-size: 58px; }
  .tagline { color: var(--grey); font-size: 12px; font-weight: 300; letter-spacing: .4px; }
  .front .tagline { position: absolute; left: 32px; top: 116px; }
  .front .band {
    position: absolute; left: 0; right: 0; top: 152px; height: 114px;
    background: linear-gradient(180deg, var(--blue-light), var(--blue));
  }
  .rule { position: absolute; left: 0; right: 0; height: 2px; background: var(--green); }
  .front .rule.top { top: 145px; }
  .front .rule.bottom { top: 273px; }
  .contacts {
    position: absolute; left: 30px; bottom: 16px;
    list-style: none; color: var(--white); font-size: 14px; line-height: 1.55;
  }
  .contacts li { display: flex; align-items: center; gap: 9px; }
  .contacts svg { width: 14px; height: 14px; flex: none; }
  .address {
    position: absolute; right: 30px; top: 18px;
    color: var(--white); font-size: 14px; text-align: right; line-height: 1.5;
  }

  /* Back: logo side */
  .back { background: linear-gradient(180deg, var(--blue-deep), var(--blue-light) 50%, var(--blue-deep)); }
  .back .stripe {
    position: absolute; left: 0; right: 0; top: 100px; height: 110px;
    background: var(--paper);
  }
  .back .rule.top { top: 106px; }
  .back .rule.bottom { top: 202px; }
  .back .logo-lockup {
    position: absolute; left: 0; right: 0; top: 118px;
    display: flex; flex-direction: column; align-items: center;
  }
  .back .wordmark { font-size: 54px; }
  .back .tagline { margin-top: 4px; }
</style>
</head>
<body>

<section class="card front" aria-label="Business card, contact side">
  <div class="name-block">
    <div class="person">DANA REYES</div>
    <div class="role">Manager</div>
  </div>
  <div class="wordmark"><span>Nimbra</span><span class="dot"></span></div>
  <div class="tagline">Clear Voice Networking Made Simple</div>

  <div class="rule top"></div>
  <div class="band">
    <div class="address">Your Address, 2nd Ste<br>Maple Grove, Ohio 4410</div>
    <ul class="contacts">
      <li>
        <svg viewBox="0 0 14 14"><rect width="14" height="14" rx="2" fill="#fff" opacity=".9"/><path d="M4 3.5l1.6-.5 1 2.2-1 .8a5 5 0 0 0 2.4 2.4l.8-1 2.2 1-.5 1.6C7.5 10 4 6.5 4 3.5z" fill="#11b3e0"/></svg>
        555 014 2290
      </li>
      <li>
        <svg viewBox="0 0 14 14"><rect width="14" height="14" rx="2" fill="#fff" opacity=".9"/><rect x="3" y="4.5" width="8" height="5.5" fill="none" stroke="#11b3e0" stroke-width="1"/><path d="M3 4.5l4 3 4-3" fill="none" stroke="#11b3e0" stroke-width="1"/></svg>
        hello@nimbracloud.com
      </li>
      <li>
        <svg viewBox="0 0 14 14"><rect width="14" height="14" rx="2" fill="#fff" opacity=".9"/><circle cx="7" cy="7" r="4" fill="none" stroke="#11b3e0" stroke-width="1"/><ellipse cx="7" cy="7" rx="1.7" ry="4" fill="none" stroke="#11b3e0" stroke-width="1"/><path d="M3 7h8" stroke="#11b3e0" stroke-width="1"/></svg>
        www.nimbracloud.com
      </li>
    </ul>
  </div>
  <div class="rule bottom"></div>
</section>

<section class="card back" aria-label="Business card, logo side">
  <div class="stripe"></div>
  <div class="rule top"></div>
  <div class="rule bottom"></div>
  <div class="logo-lockup">
    <div class="wordmark"><span>Nimbra</span><span class="dot"></span></div>
    <div class="tagline">Clear Voice Networking Made Simple</div>
  </div>
</section>

</body>
</html>
```